Business logo & card design needed

We need a business logo & card design for a new company in NSW called 'Tallow Ridge Solutions'.
The company provides electrical services such as; electrical/refrigeration & air conditioning/data/security/audio visual entertainment/design & install.
We would like a logo which can relate to the electrical industry.
Updates

Industry/Entity Type

Electrical

Contact Information for Business Card

Tallow Ridge Solutions
Lira Mostfeld, Ph: 0471958360, Lic: 562930K

Logo Text

Tallow Ridge Solutions

Logo styles of interest
Emblem Logo
Abstract Logo
Wordmark Logo
Requirements
Must have
• The card must include the services we provide; electrical/refrigeration & air conditioning/data/security/audio visual entertainment/design & install.
It must also include the licence number; Lic: 562930K

```html
<!DOCTYPE html>
<html lang="en">
<head>
<meta charset="UTF-8">
<title>Tallow Ridge Solutions – Business Card</title>
<link rel="stylesheet" href="https://fonts.googleapis.com/css2?family=Open+Sans:wght@400;600&display=swap">
<style>
  :root {
    --navy: #0f4a7e;
    --navy-tint: rgba(255, 255, 255, 0.08);
    --white: #ffffff;
    --paper-top: #ffffff;
    --paper-bottom: #f1f1f1;
    --stage: #ffffff;
    --edge: #dcdcdc;
  }
  * { box-sizing: border-box; margin: 0; padding: 0; }
  html, body {
    width: 1200px;
    height: 1000px;
    overflow: hidden;
    background: var(--stage);
    font-family: "Open Sans", Arial, sans-serif;
  }
  .canvas {
    position: relative;
    width: 1200px;
    height: 1000px;
  }
  .card {
    position: absolute;
    left: 320px;
    width: 560px;
    height: 320px;
    overflow: hidden;
  }
  /* Front side */
  .card--front {
    top: 150px;
    background: var(--navy);
    color: var(--white);
  }
  .card__emblem-field {
    position: absolute;
    left: 40px;
    top: 50px;
    width: 170px;
    height: 170px;
    border-radius: 50%;
    background: var(--navy-tint);
  }
  .card__person {
    position: absolute;
    left: 280px;
    top: 70px;
  }
  .card__name {
    font-size: 25px;
    font-weight: 600;
    letter-spacing: 0.2px;
    margin-bottom: 14px;
  }
  .card__detail {
    font-size: 16px;
    font-weight: 400;
    letter-spacing: 1px;
    line-height: 1.35;
    padding-left: 12px;
  }
  .card__services {
    position: absolute;
    right: 28px;
    bottom: 24px;
    text-align: right;
    font-size: 13px;
    letter-spacing: 0.9px;
    line-height: 1.4;
  }
  /* Back side */
  .card--back {
    top: 530px;
    background: linear-gradient(160deg, var(--paper-top) 40%, var(--paper-bottom));
    border: 1px solid var(--edge);
  }
  .brand {
    position: absolute;
    left: 0;
    right: 0;
    top: 118px;
    display: flex;
    align-items: center;
    justify-content: center;
    gap: 14px;
  }
  .brand__dot {
    width: 16px;
    height: 16px;
    border-radius: 50%;
    background: var(--navy);
  }
  .brand__name {
    color: var(--navy);
    font-size: 26px;
    font-weight: 400;
    letter-spacing: 2px;
    text-transform: uppercase;
  }
  .card__web {
    position: absolute;
    left: 0;
    right: 0;
    bottom: 34px;
    text-align: center;
    color: var(--navy);
    font-size: 12px;
    letter-spacing: 0.5px;
  }
</style>
</head>
<body>
<main class="canvas">
  <section class="card card--front" aria-label="Card front">
    <div class="card__emblem-field" aria-hidden="true"></div>
    <div class="card__person">
      <p class="card__name">Lira Mostfeld</p>
      <p class="card__detail">Ph: 0471958360</p>
      <p class="card__detail">Lic: 562930K</p>
    </div>
    <p class="card__services">
      electrical • refrigeration &amp; air conditioning • data<br>
      security • audio visual entertainment • design &amp; install
    </p>
  </section>

  <section class="card card--back" aria-label="Card back">
    <div class="brand">
      <span class="brand__dot" aria-hidden="true"></span>
      <span class="brand__name">Tallow Ridge Solutions</span>
    </div>
    <p class="card__web">www.tallowridgesolutions.com.au</p>
  </section>
</main>
</body>
</html>
```